Company Mission & Values Poster

I'd like an A2 Portrait Poster displaying our company's Mission & Values.
See our website for our logo, fonts, mission & values.
https://talvendo.com.au/

Our Mission: Creating homes for abundant life
Values: Love, Thinking, Team, Zoe.

Some ideas to consider:
Mission as the Headline then
A logo for each of the 4 Values and the words

Target Market(s)

Myself & my team

Industry/Entity Type

Real Estate

Font styles to use
Other font styles liked:
• Company fonts as seen on our website

```html
<!DOCTYPE html>
<html lang="en">
<head>
<meta charset="utf-8">
<title>Talvendo – Mission &amp; Values Poster</title>
<link rel="stylesheet" href="https://fonts.googleapis.com/css2?family=Bodoni+Moda:wght@400;500&family=Raleway:wght@400;500&display=swap">
<style>
  :root {
    --forest: #0b3a2c;
    --ink: #1e2a26;
    --paper: #ffffff;
    --backdrop: #ecedec;
    --rule: #9aa19e;
  }
  * { margin: 0; padding: 0; box-sizing: border-box; }
  html, body { width: 1200px; height: 1200px; overflow: hidden; }
  body {
    background: var(--backdrop);
    font-family: "Raleway", sans-serif;
    color: var(--ink);
    position: relative;
  }
  .poster {
    position: absolute;
    left: 200px; top: 35px;
    width: 800px; height: 1130px;
    background: var(--paper);
    box-shadow: 0 2px 10px rgba(0,0,0,.12);
  }
  .brand {
    position: absolute; top: 52px; left: 0; width: 100%;
    text-align: center;
    font-family: "Bodoni Moda", serif;
    font-weight: 500;
    font-size: 70px;
    letter-spacing: 10px;
    color: var(--forest);
    line-height: 1;
  }
  .header-rule {
    position: absolute; top: 169px; left: 0; width: 100%; height: 5px;
    background: var(--forest);
  }
  .header-tab {
    position: absolute; top: 172px; left: 139px; width: 496px; height: 44px;
    background: var(--forest);
    border-radius: 0 0 30px 30px;
    color: var(--paper);
    font-family: "Bodoni Moda", serif;
    font-size: 31px; letter-spacing: 2px;
    text-align: center; line-height: 46px;
  }
  .label {
    position: absolute; left: 0; width: 100%;
    text-align: center; font-size: 20px; letter-spacing: .5px;
  }
  .label--mission { top: 262px; }
  .label--values { top: 401px; }
  .mission {
    position: absolute; top: 296px; left: 0; width: 100%;
    text-align: center;
    font-family: "Bodoni Moda", serif;
    font-size: 30px; letter-spacing: 2.5px;
    color: var(--forest);
  }
  .value {
    position: absolute; left: 0; width: 100%;
  }
  .value__icon {
    position: absolute; left: 31px; top: 0;
    width: 100px; height: 100px;
  }
  .value__title {
    position: absolute; left: 161px; top: -30px;
    font-family: "Bodoni Moda", serif;
    font-size: 30px; letter-spacing: 1px;
    color: var(--ink);
    line-height: 1;
  }
  .value__title::after {
    content: ""; display: block;
    width: 52px; height: 3px; margin-top: 5px;
    background: var(--forest);
  }
  .value__text {
    position: absolute; left: 161px; top: 14px; width: 560px;
    font-size: 18px; line-height: 26px;
    text-align: justify; hyphens: auto;
  }
  .divider {
    position: absolute; left: 44px; width: 677px; height: 1.5px;
    background: var(--rule);
  }
  .footer-band {
    position: absolute; left: 0; bottom: 0; width: 100%; height: 34px;
    background: var(--forest);
  }
  .icon-stroke { fill: none; stroke: var(--forest); stroke-width: 2.4; stroke-linecap: round; stroke-linejoin: round; }
</style>
</head>
<body>
  <main class="poster">
    <div class="brand">TALVENDO</div>
    <div class="header-rule"></div>
    <div class="header-tab">MISSION &amp; VALUES</div>

    <p class="label label--mission">OUR MISSION:</p>
    <h1 class="mission">CREATING HOMES FOR ABUNDANT LIFE</h1>

    <p class="label label--values">VALUES:</p>

    <section class="value" style="top:432px">
      <svg class="value__icon" viewBox="0 0 100 100" aria-hidden="true">
        <circle class="icon-stroke" cx="50" cy="50" r="47"/>
        <path class="icon-stroke" d="M54 44 C42 35 38 28 44 23 C48 20 52 22 54 26 C56 22 60 20 64 23 C70 28 66 35 54 44Z"/>
        <path class="icon-stroke" d="M22 52 h8 v16 h-8z M30 54 h14 c4 0 6 4 2 6 h-10 M46 60 l18 -6 c4 -1 6 3 2 5 l-20 10 h-16"/>
      </svg>
      <h2 class="value__title">LOVE</h2>
      <p class="value__text">Our mission is founded in our love and respect for people - those we develop for, those in our teams and those in the communities we create and operate within.</p>
    </section>
    <div class="divider" style="top:558px"></div>

    <section class="value" style="top:598px">
      <svg class="value__icon" viewBox="0 0 100 100" aria-hidden="true">
        <circle class="icon-stroke" cx="50" cy="50" r="47"/>
        <path class="icon-stroke" d="M50 30 c-10 0 -16 8 -14 17 c1 5 6 8 7 14 h14 c1 -6 6 -9 7 -14 c2 -9 -4 -17 -14 -17z"/>
        <path class="icon-stroke" d="M44 66 h12 M45 71 h10 M47 76 h6 M50 61 v-12 l-4 -4 M50 49 l4 -4"/>
        <path class="icon-stroke" d="M50 16 v6 M30 24 l4 5 M70 24 l-4 5 M22 42 h6 M72 42 h6 M24 58 l5 -2 M76 58 l-5 -2"/>
      </svg>
      <h2 class="value__title">THINKING</h2>
      <p class="value__text">We believe in the power of thinking. Our rigorous and creative processes create beautifully considered solutions for our purchasers, the communities we develop within and the environment.</p>
    </section>
    <div class="divider" style="top:726px"></div>

    <section class="value" style="top:765px">
      <svg class="value__icon" viewBox="0 0 100 100" aria-hidden="true">
        <circle class="icon-stroke" cx="50" cy="50" r="47"/>
        <circle class="icon-stroke" cx="50" cy="30" r="8"/>
        <circle class="icon-stroke" cx="32" cy="62" r="8"/>
        <circle class="icon-stroke" cx="68" cy="62" r="8"/>
        <path class="icon-stroke" d="M44 38 l-6 16 M56 38 l6 16 M40 62 h20"/>
      </svg>
      <h2 class="value__title">TEAM</h2>
      <p class="value__text">Property development is a team sport. We surround ourselves with the best designers and advisers. We strive to create an environment that allows them to do their best work and love doing it.</p>
    </section>
    <div class="divider" style="top:900px"></div>

    <section class="value" style="top:938px">
      <svg class="value__icon" viewBox="0 0 100 100" aria-hidden="true">
        <circle class="icon-stroke" cx="50" cy="50" r="47"/>
        <path class="icon-stroke" d="M54 46 v-10 M54 36 c-10 -2 -14 -8 -12 -14 c8 1 12 6 12 14z M54 40 c8 -1 12 -6 11 -12 c-7 0 -11 5 -11 12z"/>
        <path class="icon-stroke" d="M22 52 h8 v16 h-8z M30 54 h14 c4 0 6 4 2 6 h-10 M46 60 l18 -6 c4 -1 6 3 2 5 l-20 10 h-16"/>
      </svg>
      <h2 class="value__title">ZOE</h2>
      <p class="value__text">Our mission is to create places for ‘Zoe’ - the Greek word for abundant life. We do this through exquisite design, quality construction and celebrating nature.</p>
    </section>

    <div class="footer-band"></div>
  </main>
</body>
</html>
```